Tolvane BrandWorks Corporate Site

Design a site to replace www.tolvanebrandworks.com, built for/within net harbor and incorporate numerous corporate assets and lines of business (www.pulsarstageworksinc.com, www.summitoutingpros.com, www.zapsnapkiosk.com, www.nibblecrate.com, www.strumbleorama.com) as well as our consulting and artist management work.

Target Market(s)

businesses, non profits, talent (performing artists)

Industry/Entity Type

Business

Coding

Coded - Design and coding required

Number of Pages Required

5+ page

Colors
0655a3
ffc214

Requirements
Must have
• social media visibility, multi-media

```html
<!DOCTYPE html>
<html lang="en">
<head>
<meta charset="utf-8">
<title>Tolvane BrandWorks</title>
<link href="https://fonts.googleapis.com/css2?family=Raleway:wght@400;600;700;800&family=Open+Sans:wght@400;600;700&display=swap" rel="stylesheet">
<style>
:root{
  --navy:#0b2f6b;
  --blue:#0655a3;
  --gold:#ffc214;
  --ink:#333;
  --muted:#666;
  --dark:#1c1c1e;
  --hero-a:#f2f3f5;
  --hero-b:#d9dce1;
  --line:#e3e3e3;
}
*{margin:0;padding:0;box-sizing:border-box}
html,body{width:826px;height:1200px;overflow:hidden;background:#fff}
body{font-family:"Open Sans",sans-serif;color:var(--ink);position:relative}
.header{height:56px;display:flex;align-items:center;justify-content:space-between;padding:0 0 0 36px;background:#fff}
.brand-name{font-family:"Raleway",sans-serif;font-weight:700;font-size:22px;color:var(--navy);line-height:1}
.brand-tag{font-family:"Raleway",sans-serif;font-weight:700;font-size:22px;color:var(--navy);display:none}
.brand-sub{font-size:7px;letter-spacing:1.4px;color:var(--blue);margin-top:4px;text-transform:uppercase}
.nav{display:flex;height:56px;margin-right:70px}
.nav a{display:flex;align-items:center;padding:0 12px;font-family:"Raleway",sans-serif;font-size:8.5px;font-weight:700;color:var(--navy);text-decoration:none;letter-spacing:.4px}
.nav a.active{background:var(--navy);color:#fff}
.hero{position:absolute;top:56px;left:0;width:826px;height:410px;background:linear-gradient(180deg,var(--hero-a),var(--hero-b))}
.hero-copy{position:absolute;top:200px;left:0;width:100%;text-align:center}
.hero h1{font-family:"Raleway",sans-serif;font-weight:800;font-size:36px;line-height:1.12;color:var(--navy);letter-spacing:.5px}
.hero p{width:420px;margin:12px auto 0;font-size:10px;line-height:1.5;color:#222;background:rgba(255,255,255,.55)}
.btn{display:inline-block;background:var(--navy);color:#fff;font-family:"Raleway",sans-serif;font-size:8px;font-weight:700;padding:9px 18px;letter-spacing:.5px}
.hero .btn{margin-top:14px}
.services{position:absolute;top:466px;left:0;width:826px;height:184px;background:var(--dark);display:flex}
.service{flex:1;text-align:center;padding:38px 40px 0;color:#ddd}
.service h3{font-family:"Raleway",sans-serif;font-size:14px;font-weight:600;color:var(--gold);margin:10px 0 8px}
.service p{font-size:9px;line-height:1.5}
.service.featured{background:var(--navy);margin-top:-22px;padding-top:58px;height:206px}
.service.featured h3{color:#fff}
.service.featured .btn{background:none;margin-top:12px;padding:0}
.about{position:absolute;top:680px;left:32px;width:410px}
.about h2{font-family:"Raleway",sans-serif;font-weight:600;font-size:22px;color:var(--navy);margin-bottom:14px}
.about p{font-size:9.5px;line-height:1.65;color:var(--muted);margin-bottom:10px}
.about .btn{margin-top:8px}
.news{position:absolute;top:680px;left:472px;width:320px}
.news h2{font-family:"Raleway",sans-serif;font-weight:600;font-size:22px;color:var(--navy);margin-bottom:12px}
.news-item{display:flex;gap:14px;padding:10px 0;border-bottom:1px solid var(--line)}
.news-thumb{width:64px;height:64px;flex:none;background:linear-gradient(160deg,#b8a89a,#5d5048)}
.news-date{font-size:8px;color:#999}
.news-item h4{font-size:9.5px;font-weight:700;color:var(--ink);margin:3px 0 4px}
.news-item p{font-size:8.5px;line-height:1.5;color:var(--muted)}
.video{position:absolute;top:945px;left:0;width:826px;height:195px;background:linear-gradient(100deg,#3b2a14,#151515 55%,#252a33)}
.video-copy{position:absolute;top:28px;left:32px;width:380px}
.video h2{font-family:"Raleway",sans-serif;font-weight:400;font-size:34px;color:var(--gold)}
.video p{font-size:9.5px;line-height:1.55;color:#ddd;margin:8px 0 14px}
.video-frame{position:absolute;top:26px;left:440px;width:380px;height:144px;background:linear-gradient(135deg,#4a4f58,#23262c)}
.play{position:absolute;top:48px;left:162px}
.footer{position:absolute;top:1140px;left:0;width:826px;height:60px;background:var(--navy);display:flex;align-items:center;justify-content:center}
.footer p{font-size:9px;color:#fff}
.social{position:absolute;right:20px;top:22px;display:flex;gap:6px}
.social span{width:16px;height:16px;background:#fff}
</style>
</head>
<body>
<header class="header">
  <div class="brand">
    <div class="brand-name">Tolvane BrandWorks</div>
    <div class="brand-sub">Integrated Marketing &amp; Communications</div>
  </div>
  <nav class="nav">
    <a class="active">HOME</a><a>ABOUT</a><a>OUR SERVICES</a><a>CLIENTS</a><a>NEWS &amp; EVENTS</a><a>BLOG</a><a>CONTACT</a>
  </nav>
</header>

<section class="hero" role="img" aria-label="Crowd of business people standing on a pale floor, seen from above">
  <div class="hero-copy">
    <h1>WELCOME TO<br>TOLVANE BRANDWORKS</h1>
    <p>Lorem ipsum dolor sit amet, consectetur adipiscing elit, sed do eiusmod tempor incididunt ut labore et dolore magna aliqua. Ut enim ad minim veniam, quis nostrud exercitation ullamco laboris nisi ut aliquip ex ea commodo consequat.</p>
    <span class="btn">READ MORE</span>
  </div>
</section>

<section class="services">
  <div class="service">
    <svg width="20" height="20" viewBox="0 0 20 20" fill="none" stroke="#ffc214" stroke-width="1.6"><path d="M3 8h4l7-4v12l-7-4H3z"/><path d="M6 12l1 5"/></svg>
    <h3>Public Relations</h3>
    <p>Lorem ipsum dolor sit amet, consectetur adipiscing elit, sed do eiusmod tempor incididunt ut labore et dolore magna aliqua.</p>
  </div>
  <div class="service featured">
    <svg width="20" height="20" viewBox="0 0 20 20" fill="none" stroke="#fff" stroke-width="1.6"><circle cx="10" cy="10" r="7"/><path d="M10 3v14M3 10h14"/></svg>
    <h3>Strategic Marketing</h3>
    <p>Lorem ipsum dolor sit amet, consectetur adipiscing elit, sed do eiusmod tempor incididunt ut labore et dolore magna aliqua.</p>
    <span class="btn">READ MORE</span>
  </div>
  <div class="service">
    <svg width="20" height="20" viewBox="0 0 20 20" fill="none" stroke="#ffc214" stroke-width="1.6"><circle cx="7" cy="7" r="3"/><circle cx="14" cy="8" r="2.5"/><path d="M2 17c0-4 3-6 5-6s5 2 5 6M12 13c2-1 6 0 6 4"/></svg>
    <h3>Multicultural Marketing</h3>
    <p>Lorem ipsum dolor sit amet, consectetur adipiscing elit, sed do eiusmod tempor incididunt ut labore et dolore magna aliqua.</p>
  </div>
</section>

<section class="about">
  <h2>Communicate ˚ Collaborate ˚ Celebrate</h2>
  <p>In our marketing and communications we connect brands with the people who matter most, building campaigns that are creative, consistent and measurable across every channel our clients use.</p>
  <p>We work with businesses, non profits and performing artists to shape their stories, grow their audiences and bring each idea from a first sketch to a finished launch.</p>
  <p>Since day one our team has combined consulting, events and artist management under one roof, so every project has the support it needs.</p>
  <span class="btn">READ MORE</span>
</section>

<section class="news">
  <h2>Latest News</h2>
  <div class="news-item">
    <div class="news-thumb" role="img" aria-label="Portrait photo of a team member"></div>
    <div>
      <div class="news-date">12 Aug 2016</div>
      <h4>LOREM IPSUM DOLOR SIT AMET</h4>
      <p>Lorem ipsum dolor sit amet, consectetur adipiscing elit, sed do eiusmod tempor incididunt ut labore et dolore.</p>
    </div>
  </div>
  <div class="news-item">
    <div class="news-thumb" role="img" aria-label="Portrait photo of a team member"></div>
    <div>
      <div class="news-date">12 Aug 2016</div>
      <h4>LOREM IPSUM DOLOR SIT AMET</h4>
      <p>Lorem ipsum dolor sit amet, consectetur adipiscing elit, sed do eiusmod tempor incididunt ut labore et dolore.</p>
    </div>
  </div>
</section>

<section class="video" role="img" aria-label="Dim photo of a hand holding a phone playing a video">
  <div class="video-copy">
    <h2>Video</h2>
    <p>Lorem ipsum dolor sit amet, consectetur adipiscing elit, sed do eiusmod tempor incididunt ut labore et dolore magna aliqua. Ut enim ad minim veniam, quis nostrud exercitation ullamco.</p>
    <span class="btn">VIEW ALL</span>
  </div>
  <div class="video-frame">
    <svg class="play" width="52" height="52" viewBox="0 0 52 52"><circle cx="26" cy="26" r="24" fill="none" stroke="#fff" stroke-width="2.5" opacity=".85"/><path d="M21 16l16 10-16 10z" fill="#fff" opacity=".85"/></svg>
  </div>
</section>

<footer class="footer">
  <p>Copyright 2016 Tolvane BrandWorks. All Rights Reserved.</p>
  <div class="social"><span></span><span></span><span></span></div>
</footer>
</body>
</html>
```